Maplecrest Apartments Downtown Northport

We are looking to redesign our entry way sign at Maplecrest Apartments, a low density residential apartment building, located in Downtown Northport, Alabama, U.S. Downtown Northport is a bustling boutique business district with a small town feel comprised of shops, restaurants, and a renowned arts community known for Varrow Arts Center and Festival which is one of the nation's top outdoor arts festivals. Maplecrest Apartments and its sign is the first thing you seen when you enter Downtown Northport. We are looking to redesign our sign, entry way and landscaping to compliment the building and character of the historic downtown.

Target Market(s)

Our apartment building is comprised of 20 apartments units with tenants who are primarily part of the local workforce, young professionals, or students at the Halverton College or other nearby institutions.

Requirements
Must have
• The name of the apartment building - Maplecrest
Phone number on the sign 205-555-0148

```html
<!DOCTYPE html>
<html lang="en">
<head>
<meta charset="utf-8">
<title>Maplecrest Entry Sign</title>
<link rel="stylesheet" href="https://fonts.googleapis.com/css2?family=Bebas+Neue&family=Montserrat:wght@700&display=swap">
<style>
  :root {
    --page-bg: #e6e7e9;
    --sign-white: #ffffff;
    --violet-deep: #3e3d82;
    --violet-mid: #5c3684;
    --plum: #6d2e82;
    --magenta: #7d2a7f;
    --navy-band-top: #4a3382;
    --navy-band-bottom: #233c7c;
    --dot-pink: #c678c0;
    --text-white: #ffffff;
  }
  html, body {
    margin: 0;
    padding: 0;
    width: 926px;
    height: 1200px;
    overflow: hidden;
    background: var(--page-bg);
  }
  .canvas {
    position: relative;
    width: 926px;
    height: 1200px;
  }
  .entry-sign {
    position: absolute;
    left: 63px;
    top: 413px;
    width: 800px;
    height: 374px;
    filter: drop-shadow(10px 10px 6px rgba(0,0,0,0.85));
  }
  .sign-phone {
    font-family: "Montserrat", sans-serif;
    font-weight: 700;
    font-size: 122px;
    fill: var(--text-white);
  }
  .sign-name {
    font-family: "Bebas Neue", sans-serif;
    font-size: 310px;
    fill: var(--text-white);
  }
</style>
</head>
<body>
<main class="canvas">
  <svg class="entry-sign" viewBox="0 0 1295 606" xmlns="http://www.w3.org/2000/svg" aria-label="Maplecrest entry sign">
    <defs>
      <linearGradient id="upper-field" x1="0" y1="0" x2="1" y2="0">
        <stop offset="0" stop-color="var(--plum)"/>
        <stop offset="0.45" stop-color="var(--violet-mid)"/>
        <stop offset="1" stop-color="var(--plum)"/>
      </linearGradient>
      <linearGradient id="lower-field" x1="0" y1="0" x2="1" y2="0">
        <stop offset="0" stop-color="var(--violet-deep)"/>
        <stop offset="1" stop-color="var(--plum)"/>
      </linearGradient>
      <linearGradient id="phone-band" x1="0" y1="0" x2="0" y2="1">
        <stop offset="0" stop-color="var(--navy-band-top)"/>
        <stop offset="1" stop-color="var(--navy-band-bottom)"/>
      </linearGradient>
    </defs>

    <rect class="sign-board" width="1295" height="606" fill="var(--sign-white)"/>

    <polygon class="field-upper" points="0,30 71,30 250,130 1295,130 1295,420 0,420" fill="url(#upper-field)"/>
    <polygon class="accent-magenta" points="0,30 71,30 250,130 410,420 0,420" fill="var(--magenta)"/>
    <rect class="field-lower" x="0" y="418" width="1295" height="188" fill="url(#lower-field)"/>

    <polygon class="accent-dots-area" role="img" aria-label="Halftone dot accent stripe"
             points="140,95 200,95 460,380 400,380" fill="var(--dot-pink)" opacity="0.25"/>

    <polygon class="phone-band" points="168,43 1123,43 1273,207 308,207" fill="url(#phone-band)"/>

    <text class="sign-phone" x="728" y="178" text-anchor="middle">205-555-0148</text>
    <text class="sign-name" x="98" y="497" textLength="1147" lengthAdjust="spacing">MAPLECREST</text>
  </svg>
</main>
</body>
</html>
```